Time for a better IT consulting company?

We are a mobile computer consulting company, taking care of client's issues remotely or at their site. Website of company www.harbor-techmend.com. Business card is an example of marketing so far.
We moved this year but we still service our existing clients. We have expanded our number of technicians available. We would like to use this card for both new business and reaching out to old business.

Target Market(s)

This should target businesses and referrals to businesses from our existing clients as well as a new client outreach for our new location.

Industry/Entity Type

Computer

Requirements
Must have
• This postcard will let clients know we have moved into or we continue to service their area. Make sure it says Inc, not LLC. Must incorporate existing theme in some fashion.
Nice to have
• Themes to communicate: team of people standing by, stability, faster response time, accessibility.
• Areas of coverage: Westchester, Rockland, Manhattan, The Bronx, lower Connecticut.
Should not have
• Cartoon feel.

```html
<!DOCTYPE html>
<html lang="en">
<head>
<meta charset="utf-8">
<title>Harbor Crest Computer Consulting – Postcard</title>
<link rel="stylesheet" href="https://fonts.googleapis.com/css2?family=Open+Sans:ital,wght@0,400;0,600;1,400&family=Tinos&display=swap">
<style>
:root{
  --stage:#e6e6e6;
  --paper:#ffffff;
  --band-dark:#8a8a8a;
  --band-light:#e0e1e1;
  --ink-black:#0b0b0b;
  --ink-white:#ffffff;
  --ink-grey:#555555;
  --ink-soft:#9a9a9a;
  --accent:#2ba3d6;
  --accent-deep:#1a6f9e;
}
*{box-sizing:border-box;margin:0;padding:0}
html,body{width:1200px;height:536px;overflow:hidden;background:var(--stage)}
.canvas{position:relative;width:1200px;height:536px}
.card{position:absolute;top:47px;width:532px;height:412px;background:var(--paper);overflow:hidden;box-shadow:6px 7px 8px rgba(0,0,0,.45)}
.card--front{left:64px}
.card--back{left:621px;width:531px}
.band{position:absolute;left:0;width:100%}
.band--headline{top:57px;height:44px;background:linear-gradient(#9a9a9a,var(--band-dark))}
.band--plain{top:57px;height:44px;background:var(--band-light)}
.notice{position:absolute;left:45px;top:14px;width:445px;font:600 15px/18px "Open Sans",sans-serif;color:var(--accent-deep)}
.notice small{display:block;font:400 11.5px/16px "Open Sans",sans-serif;color:var(--ink-grey)}
.coverage{position:absolute;left:19px;top:16px;width:495px;font:11.5px/16px "Open Sans",sans-serif;color:var(--ink-grey)}
.coverage strong{font-weight:600;color:var(--accent-deep)}
.coverage--areas{top:70px;color:#444}
.headline{position:absolute;left:45px;top:69px;font:19px "Tinos",serif;color:var(--ink-white)}
.hero{position:absolute;left:0;top:101px;width:100%;height:178px;background:var(--ink-black)}
.hero__visual{position:absolute;left:261px;top:0;width:271px;height:178px;background:radial-gradient(ellipse at 55% 55%,#5fb8e0 0%,#1b4f73 30%,#0d1a26 65%,#050505 100%)}
.hero__copy{position:absolute;left:45px;top:12px;width:202px;font:13px/17.2px "Tinos",serif;color:var(--ink-white)}
.phone{position:absolute;left:45px;top:132px;display:flex;align-items:center;gap:7px;font:26px "Tinos",serif;color:var(--ink-white)}
.stripes{position:absolute;left:0;top:279px;width:100%;height:20px}
.contact{position:absolute;left:45px;top:321px;width:318px}
.contact__title{font:600 17px "Open Sans",sans-serif;color:var(--ink-grey);padding-bottom:1px;border-bottom:1px solid #b5b5b5}
.contact__lines{margin-top:3px;font:10px/15.5px "Tinos",serif;color:var(--ink-grey)}
.brand{position:absolute;display:flex;flex-direction:column;align-items:center;gap:7px;font:600 11px/1.25 "Open Sans",sans-serif;color:var(--accent-deep);text-align:center;white-space:nowrap}
.brand__mark{width:42px;height:42px;border-radius:50%;background:var(--accent)}
.card--front .brand{left:372px;top:306px;width:150px}
.card--back .brand{left:370px;top:298px;width:150px}
.services{position:absolute;left:0;top:101px;width:261px;height:311px;background:var(--ink-black)}
.services__title{position:absolute;left:19px;top:22px;font:16px "Open Sans",sans-serif;color:var(--ink-white);word-spacing:3px}
.services__list{position:absolute;left:30px;top:54px;list-style:none;font:11px/18.5px "Open Sans",sans-serif;color:#e8e8e8}
.services__note{position:absolute;left:20px;top:205px;width:232px;text-align:center;font:italic 12.5px/17px "Open Sans",sans-serif;color:#d8d8d8}
.footer-rule{position:absolute;left:39px;top:384px;width:323px;border-top:1px solid #555}
.footer-url{position:absolute;left:45px;top:388px;font:9px "Tinos",serif;color:var(--ink-soft)}
</style>
</head>
<body>
<main class="canvas">

  <section class="card card--front" aria-label="Postcard front">
    <p class="notice">We've moved – and we still service your area.<small>More technicians standing by for faster on-site and remote response.</small></p>
    <div class="band band--headline"></div>
    <h1 class="headline">Need immediate assistance with a computer issue?</h1>
    <div class="hero">
      <div class="hero__visual" role="img" aria-label="Photo of a hand holding a glowing laptop surrounded by floating technology icons"></div>
      <p class="hero__copy">We offer on-site business &amp; residential service &amp; repair including: emergency services, IT staffing, IP phones, hardware/software, security reviews, and web development for Mac and PC.</p>
      <p class="phone">
        <svg width="30" height="30" viewBox="0 0 30 30" aria-hidden="true">
          <circle cx="15" cy="15" r="13" fill="none" stroke="#fff" stroke-width="2"/>
          <path d="M10 8.5c1-.8 2-.6 2.5.4l1.2 2.4c.3.7.1 1.3-.5 1.8l-.9.7c.8 1.8 2.2 3.3 4 4.2l.8-.9c.5-.6 1.2-.7 1.8-.4l2.4 1.3c.9.5 1 1.5.3 2.4-1 1.3-2.5 1.8-4.1 1.2-4-1.5-7-4.6-8.3-8.6-.5-1.7 0-3.3 1.3-4.5z" fill="#fff"/>
        </svg>
        914-555-0187
      </p>
    </div>
    <svg class="stripes" viewBox="0 0 532 20" preserveAspectRatio="none" aria-hidden="true">
      <rect x="0" y="0" width="532" height="3" fill="#8fd3f0"/>
      <rect x="0" y="4" width="532" height="5" fill="#1a6f9e"/>
      <rect x="0" y="10" width="532" height="3" fill="#2ba3d6"/>
      <rect x="0" y="14" width="532" height="6" fill="#111"/>
    </svg>
    <div class="contact">
      <h2 class="contact__title">Contact Us</h2>
      <p class="contact__lines">Harbor Crest Computer Consulting<br>info@harbor-techmend.com<br>harbor-techmend.com</p>
    </div>
    <div class="brand"><span class="brand__mark"></span><span>HARBOR CREST<br>COMPUTER CONSULTING, INC</span></div>
  </section>

  <section class="card card--back" aria-label="Postcard back">
    <p class="coverage"><strong>New location, same trusted team.</strong> We continue to serve all existing clients.</p>
    <div class="band band--plain"></div>
    <p class="coverage coverage--areas"><strong>Areas covered:</strong> Westchester · Rockland · Manhattan · The Bronx · Lower Connecticut</p>
    <div class="services">
      <h2 class="services__title">Service Offered</h2>
      <ul class="services__list">
        <li>It staffing</li>
        <li>Pc &amp; MAC</li>
        <li>Home offices</li>
        <li>Websites &amp; wiring</li>
        <li>Wireless &amp; cellular solution</li>
        <li>New Equipment upgrades &amp; Purchases</li>
        <li>Hardware, software &amp; security consulting</li>
        <li>Server &amp; system monitoring &amp; maintenance</li>
      </ul>
      <p class="services__note">The highest compliment our clients can offer are referrals.<br>Thank you for your business.</p>
    </div>
    <div class="footer-rule"></div>
    <p class="footer-url">harbor-techmend.com</p>
    <div class="brand"><span class="brand__mark"></span><span>HARBOR CREST<br>COMPUTER CONSULTING, INC</span></div>
  </section>

</main>
</body>
</html>
```